Need a Halden & Co
* logo
* word and powerpoint livery
* basic webpage

Halden & Co is a Private M&A Advisor. We want to look like http://www.brightwickadvisory.example
It needs to communicate reliabity, conservativeness and discretion.

```html
<!DOCTYPE html>
<html lang="en">
<head>
<meta charset="utf-8">
<title>Halden &amp; Co</title>
<link rel="stylesheet" href="https://fonts.googleapis.com/css2?family=Arimo:wght@400;700&family=Oswald:wght@600&family=Roboto+Condensed:wght@400&family=PT+Sans:wght@400&display=swap">
<style>
  :root {
    --brand-blue: #173f8f;
    --link-blue: #1a78d6;
    --text-grey: #555555;
    --heading-grey: #858585;
    --muted-grey: #9a9a9a;
    --nav-grey: #a5a5a5;
    --panel-grey: #f3f3f3;
    --rule-grey: #dddddd;
    --white: #ffffff;
  }
  * { margin: 0; padding: 0; box-sizing: border-box; }
  html, body { width: 1200px; height: 969px; overflow: hidden; background: var(--white); }
  body { position: relative; font-family: "Arimo", Arial, sans-serif; color: var(--text-grey); }
  a { text-decoration: none; color: inherit; }

  .site-header { position: absolute; left: 0; top: 0; width: 1200px; height: 95px; }
  .brand { position: absolute; left: 168px; top: 32px; display: flex; align-items: center; gap: 10px; }
  .brand-mark { width: 18px; height: 18px; background: var(--brand-blue); }
  .brand-name { font-family: "Arimo", Arial, sans-serif; font-weight: 400; font-size: 26px; line-height: 28px; color: var(--brand-blue); }

  .social { position: absolute; display: flex; }
  .social span { display: block; width: 13px; height: 13px; border-radius: 50%; background: #c4c4c4; }
  .header-social { left: 789px; top: 38px; }
  .header-social span { margin-right: 31px; }
  .utility-links { position: absolute; left: 919px; top: 39px; font-size: 10.5px; color: var(--muted-grey); }
  .utility-links .sep { margin: 0 8px; }

  .main-nav { position: absolute; left: 0; top: 95px; width: 1200px; height: 32px; background: var(--nav-grey); }
  .main-nav a { position: absolute; top: 10px; font-size: 13px; font-weight: 700; color: var(--white); text-transform: uppercase; }
  .search { position: absolute; left: 901px; top: 8px; width: 133px; height: 17px; background: var(--white); font-size: 11px; font-style: italic; color: #aaa; padding: 2px 0 0 8px; }

  .hero { position: absolute; left: 153px; top: 142px; width: 894px; height: 275px; background: linear-gradient(180deg, #c9d6e2 0%, #d8d5cf 45%, #7b6e62 75%, #4a4440 100%); }
  .hero-title { position: absolute; left: 344px; top: 36px; font-family: "Oswald", "Arial Narrow", sans-serif; font-weight: 600; font-size: 50px; line-height: 1; color: var(--white); letter-spacing: 0.3px; transform: scaleX(0.985); transform-origin: left; white-space: nowrap; }
  .hero-subtitle { position: absolute; left: 427px; top: 92px; font-size: 27.5px; color: var(--brand-blue); white-space: nowrap; }
  .hero-arrow { position: absolute; top: 120px; }
  .hero-dots { position: absolute; left: 412px; top: 251px; display: flex; gap: 13px; }
  .hero-dots span { width: 14px; height: 14px; border-radius: 50%; border: 2px solid var(--white); background: #333; }
  .hero-dots span.is-active { background: var(--white); }

  .welcome-title { position: absolute; left: 166px; top: 451px; font-size: 26.8px; font-weight: 700; color: var(--heading-grey); }
  .team-photo { position: absolute; left: 165px; top: 492px; width: 570px; height: 165px; background: linear-gradient(90deg, #9fc0c3 0%, #c5d6d6 40%, #6f7b85 60%, #b9cfd1 100%); }
  .welcome-copy { position: absolute; left: 167px; top: 668px; width: 575px; font-size: 14.7px; line-height: 23.7px; color: var(--text-grey); }

  .news-panel { position: absolute; left: 763px; top: 492px; width: 271px; height: 366px; background: var(--panel-grey); }
  .news-title { position: absolute; left: 17px; top: 21px; font-size: 22px; font-weight: 400; color: #444; }
  .news-item { position: absolute; left: 17px; width: 245px; }
  .news-item a { display: block; font-family: "Roboto Condensed", "Arial Narrow", sans-serif; font-size: 12.5px; line-height: 16px; color: var(--link-blue); }
  .news-date { display: block; margin-top: 9px; font-size: 12.5px; color: #444; }
  .read-more { position: absolute; left: 181px; top: 331px; font-family: "Roboto Condensed", "Arial Narrow", sans-serif; font-size: 13px; color: var(--link-blue); }

  .site-footer { position: absolute; left: 0; top: 877px; width: 1200px; height: 92px; border-top: 1px solid var(--rule-grey); }
  .footer-note { position: absolute; left: 168px; top: 17px; font-family: "PT Sans", sans-serif; font-size: 10px; line-height: 16px; color: #666; }
  .footer-links { position: absolute; left: 771px; top: 18px; font-family: "PT Sans", sans-serif; font-size: 11px; color: #555; }
  .footer-links .sep { margin: 0 5px; }
  .footer-social { left: 964px; top: 19px; }
  .footer-social span { margin-right: 11px; }
</style>
</head>
<body>
  <header class="site-header">
    <div class="brand">
      <span class="brand-mark"></span>
      <span class="brand-name">Halden &amp; Co</span>
    </div>
    <div class="social header-social" aria-label="Social links"><span></span><span></span><span></span></div>
    <div class="utility-links"><a href="#">SUPPORT</a><span class="sep">|</span><a href="#">SITEMAP</a></div>
  </header>

  <nav class="main-nav">
    <a href="#" style="left:168px">Home</a>
    <a href="#" style="left:245px">About</a>
    <a href="#" style="left:329px;top:9px">Team</a>
    <a href="#" style="left:403px">Experience</a>
    <a href="#" style="left:522px">Press Releases</a>
    <a href="#" style="left:674px">Careers</a>
    <a href="#" style="left:771px">Contact</a>
    <div class="search">Search</div>
  </nav>

  <section class="hero" role="img" aria-label="City skyline of office towers under a soft sky">
    <div class="hero-title">WE CAN BE YOUR GUIDE</div>
    <div class="hero-subtitle">In the world of financial services</div>
    <svg class="hero-arrow" style="left:8px" width="28" height="40" viewBox="0 0 28 40"><path d="M22 2 L6 20 L22 38" fill="none" stroke="#8a8a8a" stroke-width="6"/></svg>
    <svg class="hero-arrow" style="left:858px" width="28" height="40" viewBox="0 0 28 40"><path d="M6 2 L22 20 L6 38" fill="none" stroke="#8a8a8a" stroke-width="6"/></svg>
    <div class="hero-dots"><span class="is-active"></span><span></span><span></span></div>
  </section>

  <h1 class="welcome-title">Welcome to Halden &amp; Co</h1>
  <div class="team-photo" role="img" aria-label="Team of business professionals in a bright glass office"></div>
  <p class="welcome-copy">Lorem ipsum dolor sit amet, consectetuer adipiscing elit, sed diam nonummy nibh euismod tincidunt ut laoreet dolore magna aliquam erat volutpat. Ut wisi enim ad minim veniam, quis nostrud exerci tation ullamcorper suscipit lobortis nisl ut aliquip ex ea commodo consequat. Duis autem vel eum iriure dolor in hendrerit in vulputate velit esse molestie consequat, vel illum dolore eu feugiat nulla facilisis at vero eros et accumsan et iusto odio dignissim qui blandit praesent luptatum zzril delenit augue duis dolore te feugait nulla facilisi.</p>

  <aside class="news-panel">
    <h2 class="news-title">Latest News</h2>
    <div class="news-item" style="top:71px"><a href="#">Lorem ipsum dolor sit amet, consectetuer adipiscing elit, sed diam nonummy nibh</a><span class="news-date">05/09/2014</span></div>
    <div class="news-item" style="top:153px"><a href="#">euismod tincidunt ut laoreet dolore magna aliquam erat volutpat. Ut wisi enim ad minim veniam, quis nostrud</a><span class="news-date">05/09/2014</span></div>
    <div class="news-item" style="top:250px"><a href="#">Lorem ipsum dolor sit amet, consectetuer adipiscing elit, sed diam nonummy nibh</a><span class="news-date">05/09/2014</span></div>
    <a class="read-more" href="#">read more</a>
  </aside>

  <footer class="site-footer">
    <div class="footer-note">Lorem ipsum dolor sit amet, consectetuer adipiscing elit, sed diam nonummy nibh euismod tincidunt ut<br>2013 Halden &amp; Co. All Rights Reserved</div>
    <div class="footer-links"><a href="#">Home</a><span class="sep">|</span><a href="#">Site Map</a><span class="sep">|</span><a href="#">Legal</a><span class="sep">|</span><a href="#">Contact</a></div>
    <div class="social footer-social" aria-label="Social links"><span></span><span></span><span></span></div>
  </footer>
</body>
</html>
```